High end business card design for custom homebuilding company

Looking for a high end business card design that is unique and elegant. Can use embossing, foil printing, laser die cutting, or any high end printing technique or high end paper. Will upload current design so you can see the logo and what we are using currently, but we want something more unique and elegant. I included our logo to help with design.

Target Market(s)

High end custom home buyers of $1.5 million plus homes. Also real estate developers of high end communities.

Industry/Entity Type

Business

Contact Information for Business Card

Double sided. We want something very elegant and expensive looking. We are looking to incorporate a combination of perhaps linen paper or a high end paper, with foil stamping or embossing/debossing to make the card look unique, but still elegant. We tend to use blacks and golds, but are open to any ideas. Looking for creative and unique design.

Colors

Designer to choose colors to be used in the design.

Requirements
Must have
• High end, elegant look. Can use foil, embossing, or high end papers like linen. We want to make the card unique and interesting, but elegant and expensive looking.
Nice to have
• I am including just some cards I saw that looked interesting for one reason or another. I like a clean elegant design and like both the clean white style, and the blacks. So not sure if we want a black design or white. Would like to see both.

```html
<!DOCTYPE html>
<html lang="en">
<head>
<meta charset="utf-8">
<title>Harborline Custom Homes – Business Card</title>
<link rel="stylesheet" href="https://fonts.googleapis.com/css2?family=Roboto:wght@400;500;700&family=Roboto+Condensed:wght@700&display=swap">
<style>
  :root {
    --backdrop: #e4e4e4;
    --paper: #f7f7f6;
    --ink: #1d1d1b;
    --ink-soft: #555555;
    --gold: #b8a445;
    --rule: #3a3a3a;
  }
  * { box-sizing: border-box; margin: 0; padding: 0; }
  html, body { width: 1200px; height: 960px; overflow: hidden; }
  body {
    background: var(--backdrop);
    font-family: "Roboto", Arial, sans-serif;
    position: relative;
  }
  .card {
    position: absolute;
    width: 602px;
    height: 344px;
    background: var(--paper);
  }
  .card--front { left: 320px; top: 96px; }
  .card--back  { left: 320px; top: 492px; }

  /* Front */
  .brand {
    position: absolute;
    left: 0; right: 0; top: 138px;
    display: flex;
    align-items: center;
    justify-content: center;
    gap: 12px;
    font-family: "Roboto", Arial, sans-serif;
    font-weight: 500;
    font-size: 28px;
    letter-spacing: 4px;
    color: var(--ink);
  }
  .brand__dot {
    width: 26px; height: 26px;
    border-radius: 50%;
    background: var(--gold);
    flex: none;
  }
  .social {
    position: absolute;
    left: 138px; top: 278px;
    width: 328px;
    display: flex;
    align-items: center;
    gap: 4px;
  }
  .social__rule { flex: 1; height: 1px; background: var(--rule); }
  .social__rule:first-child { margin-right: 6px; }
  .social__rule:last-child { margin-left: 6px; }
  .social__dot {
    width: 23px; height: 23px;
    border-radius: 50%;
    background: var(--ink);
  }

  /* Back */
  .back-mark {
    position: absolute;
    right: 48px; top: 58px;
    display: flex;
    align-items: center;
    gap: 10px;
    font-weight: 500;
    font-size: 22px;
    letter-spacing: 3px;
    color: var(--ink);
  }
  .back-mark__dot {
    width: 22px; height: 22px;
    border-radius: 50%;
    background: var(--gold);
  }
  .person {
    position: absolute;
    left: 50px; top: 180px;
  }
  .person__name {
    font-family: "Roboto Condensed", "Roboto", Arial, sans-serif;
    font-weight: 700;
    font-size: 23px;
    color: var(--gold);
    line-height: 1;
  }
  .person__role {
    margin-top: 8px;
    font-weight: 500;
    font-size: 14px;
    color: var(--ink);
  }
  .contact {
    position: absolute;
    left: 50px; top: 242px;
    font-size: 14px;
    color: var(--ink-soft);
  }
  .contact__row {
    display: flex;
    align-items: center;
    gap: 7px;
    height: 19px;
  }
  .contact__icon { width: 13px; height: 13px; fill: var(--gold); flex: none; }
  .contact__divider {
    position: absolute;
    left: 235px; top: 263px;
    width: 1px; height: 32px;
    background: #9a9a9a;
  }
  .address {
    position: absolute;
    left: 261px; top: 261px;
    font-size: 14px;
    line-height: 19px;
    color: var(--ink-soft);
  }
</style>
</head>
<body>
  <section class="card card--front" aria-label="Card front">
    <div class="brand">
      <span class="brand__dot"></span>
      <span class="brand__name">HARBORLINE CUSTOM HOMES</span>
    </div>
    <div class="social" aria-label="Social media links">
      <span class="social__rule"></span>
      <span class="social__dot"></span>
      <span class="social__dot"></span>
      <span class="social__dot"></span>
      <span class="social__dot"></span>
      <span class="social__dot"></span>
      <span class="social__rule"></span>
    </div>
  </section>

  <section class="card card--back" aria-label="Card back">
    <div class="back-mark">
      <span class="back-mark__dot"></span>
      <span>HARBORLINE</span>
    </div>

    <div class="person">
      <p class="person__name">DANIEL AVERY</p>
      <p class="person__role">CEO/FOUNDER</p>
    </div>

    <div class="contact">
      <p class="contact__row">
        <svg class="contact__icon" viewBox="0 0 24 24" aria-hidden="true"><path d="M6.6 10.8a15.1 15.1 0 0 0 6.6 6.6l2.2-2.2c.3-.3.7-.4 1-.2 1.1.4 2.3.6 3.6.6.6 0 1 .4 1 1V20c0 .6-.4 1-1 1A17 17 0 0 1 3 4c0-.6.4-1 1-1h3.5c.6 0 1 .4 1 1 0 1.3.2 2.5.6 3.6.1.3 0 .7-.2 1z"/></svg>
        <span>555 201 4870</span>
      </p>
      <p class="contact__row">
        <svg class="contact__icon" viewBox="0 0 24 24" aria-hidden="true"><path d="M2 5h20v14H2z" opacity=".85"/><path d="M2 5l10 7 10-7" fill="none" stroke="#f7f7f6" stroke-width="2"/></svg>
        <span>daniel@harborline.com</span>
      </p>
      <p class="contact__row">
        <svg class="contact__icon" viewBox="0 0 24 24" aria-hidden="true"><circle cx="12" cy="12" r="10"/><path d="M2 12h20M12 2c3 3 3 17 0 20M12 2c-3 3-3 17 0 20" fill="none" stroke="#f7f7f6" stroke-width="1.5"/></svg>
        <span>www.harborline.com</span>
      </p>
    </div>

    <span class="contact__divider"></span>

    <p class="address">1420 Willow Crest Road<br>Juneau, Alaska 99801</p>
  </section>
</body>
</html>
```